Moving Company Needs Business Card Design

We need a business cars for moving company based in San Diego. We are called Harborline Moving Systems. We move locally and long distance. 1st side: Logo, website: www.HarborlineMoving.example, Telephone number: 1-855-314-7086.
2nd side: Licensed and Insured,
We move homes and businesses
Services: Local Moving, Long Distance Moving, Loading / Unloading your truck / container, On-site Moving, Packing Service
telephone number 1-855-314-7086, email: info@harborlinemoving.example

```html
<!DOCTYPE html>
<html lang="en">
<head>
<meta charset="utf-8">
<title>Harborline Moving Systems – Business Card</title>
<link href="https://fonts.googleapis.com/css2?family=Arimo:wght@400;700&display=swap" rel="stylesheet">
<style>
  :root {
    --brand-red: #d3212a;
    --brand-red-dark: #b81d25;
    --brand-blue: #1f4f9e;
    --card-white: #ffffff;
    --page-bg: #e4e4e4;
    --text-font: "Arimo", Arial, sans-serif;
  }
  * { box-sizing: border-box; margin: 0; padding: 0; }
  html, body { width: 1200px; height: 900px; overflow: hidden; }
  body {
    background: var(--page-bg);
    font-family: var(--text-font);
    position: relative;
  }
  .card {
    position: absolute;
    top: 290px;
    width: 560px;
    height: 320px;
    background: var(--card-white);
    overflow: hidden;
    box-shadow: 0 4px 14px rgba(0,0,0,0.22);
  }
  .card--front { left: 27px; }
  .card--back { left: 613px; }
  .card-shapes { position: absolute; inset: 0; }

  /* Wordmark */
  .wordmark {
    display: flex;
    align-items: center;
    gap: 10px;
    color: var(--brand-red);
    font-weight: 700;
    white-space: nowrap;
  }
  .wordmark-dot {
    border-radius: 50%;
    background: var(--brand-blue);
    flex: none;
  }

  /* Front */
  .front-content {
    position: absolute;
    left: 0; right: 0; top: 118px;
    display: flex;
    flex-direction: column;
    align-items: center;
  }
  .card--front .wordmark { font-size: 31px; }
  .card--front .wordmark-dot { width: 18px; height: 18px; }
  .front-contact {
    margin-top: 42px;
    text-align: center;
    color: var(--brand-blue);
    font-size: 13.5px;
    line-height: 18px;
  }

  /* Back */
  .services {
    position: absolute;
    left: 44px; top: 36px;
    color: var(--brand-blue);
  }
  .services-title { font-size: 28px; font-weight: 400; margin-bottom: 16px; }
  .services-list { list-style: none; font-size: 16px; line-height: 23px; }
  .back-contact {
    position: absolute;
    left: 44px; top: 200px;
    list-style: none;
    color: var(--brand-blue);
    font-size: 13.5px;
    line-height: 28px;
  }
  .back-contact li { display: flex; align-items: center; gap: 14px; }
  .back-contact svg { width: 14px; height: 12px; fill: var(--brand-blue); }
  .card--back .wordmark {
    position: absolute;
    right: 30px; top: 74px;
    font-size: 17px;
    gap: 7px;
  }
  .card--back .wordmark-dot { width: 11px; height: 11px; }
  .credential {
    position: absolute;
    right: 26px; top: 230px;
    color: var(--brand-blue);
    font-size: 22px;
  }
  .tagline {
    position: absolute;
    left: 0; right: 0; bottom: 22px;
    text-align: center;
    color: var(--card-white);
    font-size: 19px;
  }
</style>
</head>
<body>

  <section class="card card--front" aria-label="Business card front">
    <svg class="card-shapes" viewBox="0 0 560 320" aria-hidden="true">
      <polygon points="0,0 226,0 0,120" fill="var(--brand-red)"/>
      <line x1="232" y1="0" x2="0" y2="126" stroke="var(--brand-blue)" stroke-width="2"/>
      <polygon points="560,200 560,320 336,320" fill="var(--brand-red)"/>
      <line x1="560" y1="194" x2="326" y2="320" stroke="var(--brand-blue)" stroke-width="2"/>
    </svg>
    <div class="front-content">
      <div class="wordmark"><span class="wordmark-dot"></span>Harborline Moving Systems</div>
      <p class="front-contact">www.HarborlineMoving.example<br>1-855-314-7086</p>
    </div>
  </section>

  <section class="card card--back" aria-label="Business card back">
    <svg class="card-shapes" viewBox="0 0 560 320" aria-hidden="true">
      <path d="M0,248 Q260,300 560,262 L560,320 L0,320 Z" fill="var(--brand-red)"/>
      <path d="M0,241 Q260,293 560,255" fill="none" stroke="var(--brand-blue)" stroke-width="2"/>
    </svg>
    <div class="services">
      <h2 class="services-title">Services</h2>
      <ul class="services-list">
        <li>Local Moving</li>
        <li>Long Distance Moving</li>
        <li>Loading/Unloading your truck/container</li>
        <li>On-site Moving, Packing Service</li>
      </ul>
    </div>
    <ul class="back-contact">
      <li>
        <svg viewBox="0 0 14 12" aria-label="Phone"><path d="M1,4 Q7,-1 13,4 L11,5.5 L9.5,3.5 L4.5,3.5 L3,5.5 Z M4,6 L10,6 L12,11 L2,11 Z"/></svg>
        1-855-314-7086
      </li>
      <li>
        <svg viewBox="0 0 14 12" aria-label="Email"><path d="M0,1 H14 V11 H0 Z M1.5,2.5 L7,7 L12.5,2.5 Z" fill-rule="evenodd"/></svg>
        info@harborlinemoving.example
      </li>
    </ul>
    <div class="wordmark"><span class="wordmark-dot"></span>Harborline Moving Systems</div>
    <p class="credential">Licensed and Insured</p>
    <p class="tagline">We move homes and businesses</p>
  </section>

</body>
</html>
```